Plumbuddle Product Booklet - Content/Assets Provided...Need Inspirational layout!

We require you to design a 12 page booklet to be included with our Plumbuddle range of products.

We have a strong idea of what will go on each page and have all content ready for you (see enclosed document). We also have most of the assets available as well - also attached.

We require each page to be brimming with information but also need them to have a feeling of being uncluttered.

We need a theme running through the booklet so each page feels that is is part of the booklet and is visually consistent with all the other pages.

Deliverable will be a high quality PDF with 12 individual A5 pages in the correct order 1-12

Technical Specification:

Format:148 x 210 mm A5

Set type and images 1.5 mm away from edge
Bleed of 2 mm has to be added

So total page size of 152 x 214 mm including bleed.

Number of pages 12

The page sequence must be continuous in the PDF document.

Front cover = 1st page
All following pages = 2nd, 3rd, 4th, 5th, 6th page, etc.

Colours inside: 4/4-coloured CMYK

Print data: Not less than 300dpi as PDF in the CMYK colour range with the "ISO Coated v2 (Fogra 39 L)" colour profile for illustration printing paper and "PSO Uncoated ISO12647 (Fogra 47L)" for offset or recycling paper. Please do not use any spot colours or special colours.

Paper will be135 gsm Coated art paper (Glossy) with a staple binding.

We have included an image of a previous front/back cover design.

Files attached include: logo's; screenshot of front/back cover idea from another designer; our 'cartoon' background image that runs through all of our Plumbuddle branding; assorted photographs that could be used (please feel free to use all/none or your own imagery). Lastly there is the content document (PDF) with details of the 12 pages we need.

**Any questions - fire away! Will get back to you as soon as possible.**
Updates

First of all many thanks for those who have contributed to an initial design. For those who want to submit there are three days left so feel free to post. Looking forward to feeding back soon... Added Tuesday, January 31, 2017

Target Market(s)

The booklet will be read by those who have already purchased the item so isn't a sales document. However, it is essential that the booklet provides positive reinforcement that they have purchased the correct product and it is was the best option for their baby.

Industry/Entity Type

Baby

Font styles to use
Sans Serif

Requirements
Must have
• Inspired layout!
• Tidy, uncluttered and consistent look for all 12 pages...
• Colour palette to be based on the 'background image' provided. This image runs through all the Plumbuddle branding we have.
• Please let us know if you require any modifications to the images/assets e.g. higher resolution or queries with content provided.
Nice to have
• Additional imagery can be provided by designer - must be relevant and enhance the design. Surprise us! :o)
Should not have
• Don't want the look of a 'cookie cutter' template.

```html
<!DOCTYPE html>
<html lang="en">
<head>
<meta charset="utf-8">
<title>Articles – Booklet Spread</title>
<link href="https://fonts.googleapis.com/css2?family=Raleway:wght@300;400;500&display=swap" rel="stylesheet">
<style>
  :root {
    --teal: #5bbcc9;
    --teal-deep: #17adb3;
    --teal-soft: #86cfd8;
    --heading-teal: #4fb3bf;
    --page-blue: #c6e7ed;
    --ink: #2e2e2e;
    --white: #ffffff;
  }
  * { margin: 0; padding: 0; box-sizing: border-box; }
  html, body {
    width: 1200px; height: 851px; overflow: hidden;
    font-family: "Raleway", sans-serif; color: var(--ink);
    background: var(--white);
  }
  .spread { position: relative; width: 1200px; height: 851px; display: flex; }
  .page { position: relative; width: 600px; height: 851px; overflow: hidden; }
  .page--left { background: var(--white); }
  .page--right {
    background: linear-gradient(180deg, var(--page-blue) 0%, var(--page-blue) 45%, #e6f3f5 70%, #f4f6f6 100%);
  }
  .circles { position: absolute; left: 0; top: 0; }
  .section-title {
    position: absolute; left: 62px; top: 58px;
    font-weight: 300; font-size: 35px; color: var(--white); letter-spacing: 0.3px;
  }
  .article-title {
    font-weight: 400; color: var(--heading-teal);
    font-size: 21px; line-height: 31px;
  }
  .article-body p {
    font-weight: 300; font-size: 13.2px; line-height: 16.4px;
    text-align: justify; margin-bottom: 16.4px;
  }
  .article-body p:last-child { margin-bottom: 0; }
  .read-more { font-weight: 300; font-size: 13.2px; line-height: 16.4px; }
  .read-more a { color: #111; font-weight: 400; text-decoration: none; display: block; }
  .left-article { position: absolute; left: 216px; top: 176px; width: 323px; }
  .left-article .article-title { margin-bottom: 14px; }
  .column { position: absolute; top: 60px; }
  .column--one { left: 61px; width: 231px; }
  .column--two { left: 316px; width: 222px; }
  .feature-title {
    font-weight: 300; font-size: 20px; line-height: 24px;
    color: var(--white); margin-bottom: 16px; text-align: justify;
  }
  .photo {
    position: absolute; left: 60px; top: 500px; width: 540px; height: 351px;
    background: radial-gradient(ellipse at 60% 55%, #f2d6d2 0%, #e9b9bd 35%, rgba(240,230,228,0.7) 65%, rgba(244,246,246,0) 85%);
  }
</style>
</head>
<body>
<div class="spread">
  <section class="page page--left">
    <svg class="circles" width="260" height="400" viewBox="0 0 260 400" aria-hidden="true">
      <defs>
        <clipPath id="big-circle"><circle cx="104" cy="88" r="140"/></clipPath>
      </defs>
      <circle cx="40" cy="282" r="91" fill="var(--teal-soft)"/>
      <circle cx="104" cy="88" r="140" fill="var(--teal)"/>
      <circle cx="40" cy="282" r="91" fill="var(--teal-deep)" clip-path="url(#big-circle)"/>
    </svg>
    <h1 class="section-title">Articles</h1>

    <article class="left-article">
      <h2 class="article-title">How my baby’s reflux affected my whole family</h2>
      <div class="article-body">
        <p>Apart from the obvious anxiety and frustration parents feel when they can’t resolve a baby’s health issues or take them on themselves, there are some very subtle undercurrents that can impact on a family coping with a baby suffering with reflux.</p>
        <p>From my own personal experiences with our third child Juniper, I felt guilty that I couldn’t spend more time with my other children. At first with a newborn, it was expected that I was busy feeding, washing, sleeping alongside our new daughter, mirroring her random moments of sleep and my husband spent a lot of time making sure that our two other children received his attention when I was in this early routine. It seemed to be endless though and I found myself feeling more ‘split’ between my children as time moved on and Juniper didn’t improve.</p>
        <p>To me it seemed like too much to ask them to grow up fast and just deal with the fact that their little sister was ill. They were just as scared as us when Juniper would scream from tea time and into the late evening, but we had to show that we, as parents, were in control. Bedtime was tough because we’d be holding Juniper as well as trying to get our other two girls off to bed. Most of the time we weren’t in control and I definitely developed symptoms of depression during this period.</p>
        <p class="read-more">See the rest of the article here:<a href="#">www.tummycalm.info/family</a></p>
      </div>
    </article>
  </section>

  <section class="page page--right">
    <div class="photo" role="img" aria-label="Photograph of a baby in a pink outfit lying down while being given liquid medicine from an oral syringe"></div>

    <div class="column column--one article-body">
      <h2 class="feature-title">I knew my screaming baby had more than ‘just colic’.</h2>
      <p>As with so many first-time parents, my husband Tobias and I had a starry-eyed view of how things would be once we had our much wanted baby. So when Rowan arrived, ten days earlier than expected and following a smooth birth, we left hospital within hours, eager to start the perfect family life we anticipated.</p>
      <p>That night, after five hours of attempting to breastfeed, rocking, fan off, fan on (it was summer), Moses basket, our bed, with vest, without vest, we all finally fell into a deep sleep at 4am. This was not how it was meant to be; we were in shock.</p>
      <p>Over the next four weeks, a worrying pattern developed. After each feed, Rowan would arch his body and throw</p>
    </div>

    <div class="column column--two article-body">
      <p>his head backwards with surprising force.<br>His crying escalated from a few tears to a scared, inconsolable screeching, sometimes to the point of choking. Well-meaning midwives, health visitors, family, friends and our GP all tried to reassure us it was ‘just colic – all babies get it’. Over-the-counter remedies which others swore by raised our hopes but did not ease the problem.</p>
      <p>When we were told it would pass by three months, we were desperate; we did not know how to get through the next three hours. Racked with self-doubt about our parenting skills, we searched the internet tirelessly and read endless books. Had I eaten something which was affecting the breast milk? Was he feeding in the wrong position? Had we winded him enough?</p>
      <p class="read-more">See the rest of the article here:<a href="#">www.tummycalm.info/colic</a></p>
    </div>
  </section>
</div>
</body>
</html>
```